Maple Crest Yardworks Website Design

I need a 6 page website design for a company that Installs Synthetic Turf, Interlocking Pavers, and Patio Covers. We would like to see the design us "Landscaping Style" of a look and feel. Green, Blacks and Gray colors. Initially the website will be used the online brochure but landing pages will need to be built form this original design. Since this is brand new start up (actually offshoot form another company I was part of) we are limited on photography. We will need to use stock images until i can get installed projects photographed.This is a B2C site...targeting homeowners who are looking to expand their back yards or simply transition to maintenance free and drought tolerant yards. This is becoming very popular in California and along the Southwest United States.

Target Market(s)

Homeowners

Industry/Entity Type

Home Improvement

Coding

Coded - Design and coding required

Number of Pages Required

1 page

Font styles to use
Sans Serif

Colors
9bcb3b

Requirements
Must have
• Strong visuals and some graphic elements to illustrate the services.
• Here are some sample sites:
• https://brindlestoneworks.example
• https://www.lumagreenly.example/
• https://quorvatide.example/BackyardHavenPage
• https://otterlawnco.example
• https://www.sodvella.example/
• http://www.brookmeadtiles.example/
• https://faux-meadow-depot.example/
• https://terracehubsupply.example
• https://www.kettlebuildgroup.example

```html
<!DOCTYPE html>
<html lang="en">
<head>
<meta charset="utf-8">
<title>Maple Crest Yardworks</title>
<link href="https://fonts.googleapis.com/css2?family=Montserrat:wght@400;500;600;700;800&family=Righteous&display=swap" rel="stylesheet">
<style>
:root{
  --green:#9bcb3b;
  --green-dark:#6fa51e;
  --ink:#1c1c1c;
  --gray:#555;
  --mint:#effde6;
  --forest:#0f2d17;
  --white:#fff;
}
*{box-sizing:border-box;margin:0;padding:0}
html,body{width:1200px;height:4068px;overflow:hidden}
body{position:relative;background:var(--mint);font-family:'Montserrat',sans-serif;color:var(--ink)}
.abs{position:absolute}
.btn{position:absolute;background:var(--green);color:var(--white);border-radius:20px;font-size:13px;font-weight:500;display:flex;align-items:center;justify-content:center}
.ghost{position:absolute;left:0;width:1200px;text-align:center;font-family:'Righteous',sans-serif;color:var(--white);opacity:.85;text-shadow:0 0 14px rgba(155,203,59,.35)}
.h2{position:absolute;left:0;width:1200px;text-align:center;font-weight:700;font-size:34px}
.h2 em,.h2l em{font-style:normal;color:var(--green)}
.rule{position:absolute;height:12px}
.rule::before{content:"";position:absolute;left:0;right:0;top:5px;border-top:1px solid var(--ink)}
.rule::after{content:"v";position:absolute;left:50%;top:-6px;transform:translateX(-50%);font-size:14px;font-weight:700;background:inherit;padding:0 3px}
.rule.left::after{left:6px}
.h2l{position:absolute;font-weight:700;font-size:34px}
/* header */
.logo{left:226px;top:10px;font-weight:800;font-size:26px;line-height:1;color:var(--ink)}
.logo small{display:block;font-size:10px;font-weight:600;letter-spacing:1px;margin-top:2px}
.nav{left:476px;top:20px;display:flex;gap:43px;font-size:12px;color:#222}
.nav span:first-child{border-bottom:1px solid #222}
.hero-photo{left:0;top:0;width:1200px;height:600px}
.welcome{left:319px;top:107px;width:561px;height:351px;border:4px solid var(--green);border-radius:10px;background:rgba(40,70,20,.55);text-align:center;color:var(--white)}
.welcome h1{font-family:'Righteous',sans-serif;font-weight:400;font-size:44px;line-height:56px;margin-top:32px}
.welcome p{font-size:18px;line-height:24px;margin:22px 50px 0}
/* about */
.about-frame{left:226px;top:725px;width:343px;height:380px;background:var(--green)}
.about-photo{left:245px;top:744px;width:374px;height:374px;background:linear-gradient(180deg,#cbbca2 0%,#e9e6e0 40%,#77705f 55%,#8a6450 100%);box-shadow:0 4px 10px rgba(0,0,0,.2)}
.about-text{left:640px;top:844px;width:345px;font-size:11px;line-height:21.3px;color:var(--gray)}
/* bands */
.band{left:0;width:1200px;background:linear-gradient(90deg,#e6f5cf 0%,#b7dc6a 55%,#9bcb3b 100%)}
.band .grass{position:absolute;left:0;bottom:0;width:100%;height:70px;background:linear-gradient(180deg,rgba(155,203,59,0),#7fbf2a)}
.band h3{position:absolute;left:0;width:100%;text-align:center;font-size:32px;font-weight:700}
/* services */
.svc-photo{left:0;top:1432px;width:600px;height:588px;background:linear-gradient(180deg,#7fb3df 0%,#5e8a3c 40%,#3f6a22 62%,#b9a77e 82%,#3d6b1f 100%)}
.svc{position:absolute;left:578px;width:400px;height:66px}
.svc .num{position:absolute;left:0;top:0;width:46px;height:46px;border-radius:50%;background:var(--white);border:3px solid var(--green);box-shadow:0 0 0 4px rgba(155,203,59,.3);color:var(--green);font-weight:700;font-size:24px;display:flex;align-items:center;justify-content:center}
.svc h4{position:absolute;left:78px;top:-2px;color:var(--green);font-size:14px;font-weight:600}
.svc p{position:absolute;left:78px;top:20px;width:310px;font-size:11.5px;line-height:17px;color:var(--gray)}
/* gallery */
.tile{position:absolute}
.tile-cap{display:flex;flex-direction:column;align-items:center;justify-content:center;color:var(--white);font-size:14px;text-align:center}
.tile-cap i{width:34px;height:34px;border-radius:50%;background:var(--white);margin-bottom:8px;display:flex;align-items:center;justify-content:center}
/* testimonial */
.avatar{left:242px;top:3178px;width:196px;height:196px;border-radius:50%;background:linear-gradient(160deg,#8a7a66,#d6c6b0);border-bottom:10px solid var(--green)}
.quote-mark{left:482px;top:3195px;font-family:'Righteous',sans-serif;font-size:90px;line-height:1;color:#cfe3b0}
.quote{left:482px;top:3255px;width:440px;font-size:11.5px;line-height:17.5px;color:var(--gray)}
.by{left:830px;top:3381px;font-size:11px;color:#888}
/* footer */
.footer{left:0;top:3480px;width:1200px;height:588px}
.col-h{position:absolute;color:var(--green);font-size:19px;font-weight:500;text-align:center;width:240px}
.input{position:absolute;left:265px;width:188px;border:1px solid #557a3a;border-radius:14px;background:rgba(0,0,0,.35);color:#fff;font-size:11px;padding:6px 18px}
.addr{position:absolute;color:#e8f2e0;font-size:11px;line-height:21px;text-align:center}
.links{position:absolute;left:758px;top:3772px;width:240px;text-align:center;color:#fff;font-size:11px;line-height:26.6px}
.vline{position:absolute;top:3725px;width:1px;height:210px;background:rgba(155,203,59,.5)}
.social{position:absolute;top:3966px;left:556px;display:flex;gap:14px}
.social span{width:20px;height:20px;border-radius:50%;border:1.5px solid var(--green)}
.copy{position:absolute;left:0;top:4043px;width:1200px;text-align:center;color:#fff;font-size:11px}
</style>
</head>
<body>

<!-- HERO -->
<svg class="abs hero-photo" viewBox="0 0 1200 600" role="img" aria-label="Hero photo: grass-covered letters spelling home on a blurred green lawn background">
  <defs>
    <linearGradient id="heroG" x1="0" y1="0" x2="0" y2="1">
      <stop offset="0" stop-color="#b6dd74"/><stop offset=".5" stop-color="#5e9e24"/><stop offset="1" stop-color="#8ccc3c"/>
    </linearGradient>
  </defs>
  <path d="M0 0H1200V390C1000 520 700 585 430 585C250 585 110 555 0 510Z" fill="url(#heroG)"/>
  <path d="M0 465C120 540 260 578 430 582C280 592 120 575 0 525Z" fill="#1f1812"/>
</svg>
<div class="abs logo">MAPLE CREST<small>YARDWORKS</small></div>
<div class="abs nav"><span>Home</span><span>About Us</span><span>Our Services</span><span>Project Gallery</span><span>Contact Us</span></div>
<div class="abs welcome">
  <h1>Welcome To Maple Crest<br>Yardworks</h1>
  <p>It is a long established fact that a reader will be distracted by the readable content of a page when looking at its layout.</p>
</div>
<div class="btn" style="left:528px;top:376px;width:156px;height:36px;font-size:15px">Contact Us</div>
<svg class="abs" style="left:590px;top:507px" width="20" height="30" viewBox="0 0 20 30"><rect x="1" y="1" width="18" height="28" rx="9" fill="#fff" stroke="#9bcb3b" stroke-width="2"/><rect x="8.5" y="7" width="3" height="7" rx="1.5" fill="#555"/></svg>

<!-- ABOUT -->
<div class="ghost" style="top:612px;font-size:96px">ABOUT US</div>
<div class="abs about-frame"></div>
<div class="abs about-photo" role="img" aria-label="Photo of a stone planter with palms beside a brick paver patio"></div>
<div class="h2l" style="left:640px;top:750px">About <em>Us</em></div>
<div class="rule left" style="left:640px;top:808px;width:160px;background:var(--mint)"></div>
<p class="abs about-text">Lorem Ipsum is simply dummy text of the printing and typesetting industry. Lorem Ipsum has been the industry's standard dummy text ever since the 1500s, when an unknown printer took a galley of type and scrambled it to make a type specimen book. It has survived not only five centuries, but also the leap into electronic typesetting, remaining essentially unchanged. It was popularised in the 1960s with the release of Letraset sheets containing Lorem Ipsum passages.</p>
<div class="btn" style="left:640px;top:1061px;width:126px;height:32px">Read More</div>

<!-- BAND 1 -->
<div class="abs band" style="top:1202px;height:230px">
  <div class="grass" role="img" aria-label="Grass blades along the band edge"></div>
  <h3 style="top:36px">Would You Want to Decorate Your Home ?</h3>
  <div class="rule" style="left:438px;top:90px;width:326px;background:#bfe07e"></div>
  <div class="btn" style="left:499px;top:126px;width:202px;height:34px">Book an Appointment</div>
</div>

<!-- SERVICES -->
<div class="abs svc-photo" role="img" aria-label="Photo of a terraced backyard with a stone retaining wall, synthetic lawn and trees"></div>
<div class="h2l" style="left:643px;top:1468px">Our <em>Services</em></div>
<div class="rule left" style="left:643px;top:1524px;width:216px;background:var(--mint)"></div>
<div class="svc" style="top:1578px"><div class="num">1</div><h4>Synthetic Turf</h4><p>Lorem Ipsum is simply dummy text of the printing and typesetting industry.</p></div>
<div class="svc" style="top:1667px"><div class="num">2</div><h4>Interlocking Pavers</h4><p>Lorem Ipsum is simply dummy text of the printing and typesetting industry.</p></div>
<div class="svc" style="top:1756px"><div class="num">3</div><h4>Synthetic Turf</h4><p>Lorem Ipsum is simply dummy text of the printing and typesetting industry.</p></div>
<div class="svc" style="top:1845px"><div class="num">4</div><h4>Others Services</h4><p>Lorem Ipsum is simply dummy text of the printing and typesetting industry.</p></div>
<div class="btn" style="left:852px;top:1943px;width:124px;height:32px">Read More</div>

<!-- BAND 2 -->
<div class="abs band" style="top:2020px;height:216px">
  <div class="grass" role="img" aria-label="Grass blades along the band edge"></div>
  <h3 style="top:42px">Request A Free Estimation For Your House</h3>
  <div class="rule" style="left:438px;top:96px;width:326px;background:#bfe07e"></div>
  <div class="btn" style="left:499px;top:134px;width:202px;height:34px">Request A Free Estimation</div>
</div>

<!-- GALLERY -->
<div class="ghost" style="top:2268px;font-size:72px">Product Gallery</div>
<div class="h2" style="top:2362px">Project <em>Gallery</em></div>
<div class="rule" style="left:468px;top:2415px;width:266px;background:var(--mint)"></div>
<div class="tile" style="left:9px;top:2463px;width:182px;height:201px;background:linear-gradient(180deg,#c7b497,#7e6a57)" role="img" aria-label="Paver patio with stone planter"></div>
<div class="tile" style="left:210px;top:2463px;width:180px;height:201px;background:linear-gradient(180deg,#e9ecef,#5d6b52)" role="img" aria-label="White patio cover over outdoor seating"></div>
<div class="tile tile-cap" style="left:409px;top:2463px;width:382px;height:201px;background:linear-gradient(180deg,#6c8f5a,#3e9e2a)" role="img" aria-label="Front yard with bright synthetic lawn"><i><svg width="18" height="18" viewBox="0 0 18 18"><circle cx="7.5" cy="7.5" r="5" fill="none" stroke="#222" stroke-width="2"/><path d="M11.5 11.5L16 16" stroke="#222" stroke-width="2"/></svg></i>Some Description<br>About This Yoga</div>
<div class="tile" style="left:810px;top:2463px;width:180px;height:201px;background:linear-gradient(180deg,#b98c6c,#4f7a32)" role="img" aria-label="House entrance with pavers and turf"></div>
<div class="tile" style="left:1009px;top:2463px;width:182px;height:201px;background:linear-gradient(180deg,#dfe5e0,#4e8a2c)" role="img" aria-label="Side yard with lawn and patio cover"></div>
<div class="tile" style="left:13px;top:2686px;width:382px;height:200px;background:linear-gradient(180deg,#c9d6dd,#3d6a27)" role="img" aria-label="Backyard pergola with lounge furniture"></div>
<div class="tile" style="left:409px;top:2686px;width:182px;height:200px;background:linear-gradient(180deg,#e7e2d8,#3e7b25)" role="img" aria-label="Narrow yard with turf and white wall"></div>
<div class="tile" style="left:609px;top:2686px;width:182px;height:200px;background:linear-gradient(180deg,#8a6a55,#3a7b22)" role="img" aria-label="Stepping stones across synthetic lawn"></div>
<div class="tile" style="left:810px;top:2686px;width:381px;height:200px;background:linear-gradient(180deg,#dfe8ef,#7c7f80 45%,#3f8a28)" role="img" aria-label="Suburban house with front lawn"></div>
<div class="btn" style="left:537px;top:2927px;width:126px;height:32px">View More</div>

<!-- TESTIMONIALS -->
<div class="ghost" style="top:2998px;font-size:72px">Our Testimonials</div>
<div class="h2" style="top:3093px">Our <em>Tetimonials</em></div>
<div class="rule" style="left:464px;top:3147px;width:270px;background:var(--mint)"></div>
<div class="abs avatar" role="img" aria-label="Portrait of a satisfied customer"></div>
<div class="abs quote-mark">&ldquo;</div>
<p class="abs quote">There are many variations of passages of Lorem Ipsum available, but the majority have suffered alteration in some form, by injected humour, or randomised words which don't look even slightly believable. If you are going to use a passage of Lorem Ipsum, you need to be sure there isn't anything embarrassing hidden in the middle of text. All the Lorem Ipsum generators on the Internet tend to repeat predefined chunks as necessary, making this the first true generator on the</p>
<div class="abs by">- By Marta Quell</div>
<svg class="abs" style="left:570px;top:3418px" width="48" height="32" viewBox="0 0 48 32"><circle cx="13" cy="19" r="10" fill="#1c1c1c"/><path d="M17 19H9M12 16L9 19L12 22" stroke="#fff" stroke-width="1.5" fill="none"/><circle cx="34" cy="10" r="9" fill="#9bcb3b"/><path d="M30 10H38M35 7L38 10L35 13" stroke="#fff" stroke-width="1.5" fill="none"/></svg>

<!-- FOOTER -->
<svg class="abs footer" viewBox="0 0 1200 588" role="img" aria-label="Dark green backyard photo with a curved paver path behind the contact area">
  <defs><linearGradient id="ftG" x1="0" y1="0" x2="0" y2="1"><stop offset="0" stop-color="#1d4a22"/><stop offset="1" stop-color="#0b2410"/></linearGradient></defs>
  <path d="M0 120C300 40 520 20 700 30C900 40 1060 70 1200 110V588H0Z" fill="url(#ftG)"/>
  <path d="M700 30C900 40 1060 70 1200 110V128C1060 90 900 55 700 30Z" fill="#9bcb3b"/>
</svg>
<svg class="abs" style="left:577px;top:3508px" width="46" height="46" viewBox="0 0 46 46"><circle cx="23" cy="23" r="21" fill="#fff" stroke="#9bcb3b" stroke-width="2"/><path d="M13 27L23 17L33 27" stroke="#9bcb3b" stroke-width="3" fill="none"/></svg>
<div class="abs" style="left:0;top:3612px;width:1220px;text-align:center;color:#fff;font-size:34px;font-weight:700">Contact <span style="color:var(--green)">Us</span></div>

<div class="col-h" style="left:240px;top:3726px">Get In Touch</div>
<div class="input" style="top:3777px">Name</div>
<div class="input" style="top:3815px">Email</div>
<div class="input" style="top:3853px;height:54px">Message</div>
<div class="btn" style="left:313px;top:3920px;width:94px;height:24px;font-size:11px">Name</div>

<div class="vline" style="left:502px"></div>
<div class="col-h" style="left:512px;top:3726px">Address</div>
<div class="addr" style="left:552px;top:3770px;width:180px">88 Fernhollow Rd Ste 14<br>Tolvary County<br>2210 Larkspur Lane<br>Tolvary Bay, CA 90000</div>
<svg class="abs" style="left:551px;top:3775px" width="14" height="16" viewBox="0 0 14 16"><path d="M7 15C3 10 2 8 2 6A5 5 0 0 1 12 6C12 8 11 10 7 15Z" fill="none" stroke="#fff"/><circle cx="7" cy="6" r="1.8" fill="#fff"/></svg>
<svg class="abs" style="left:566px;top:3876px" width="16" height="16" viewBox="0 0 16 16"><path d="M3 2L6 2L7 5L5 6.5C6 9 7 10 9.5 11L11 9L14 10V13C14 14 13 14 12 14C6 13 2 9 2 4C2 3 2 2 3 2Z" fill="none" stroke="#fff"/></svg>
<div class="addr" style="left:590px;top:3874px">+00 555 014 872</div>
<svg class="abs" style="left:560px;top:3910px" width="16" height="12" viewBox="0 0 16 12"><rect x="1" y="1" width="14" height="10" fill="none" stroke="#fff"/><path d="M1 1L8 7L15 1" fill="none" stroke="#fff"/></svg>
<div class="addr" style="left:582px;top:3905px">hello@maplecrestyard.example</div>

<div class="vline" style="left:763px"></div>
<div class="col-h" style="left:758px;top:3724px">Quick Links</div>
<div class="links">Home<br>About Us<br>Our Services<br>Project Gallery<br>Privacy &amp; Policy<br>Contact Us</div>

<div class="social"><span></span><span></span><span></span><span></span><span></span></div>
<div class="copy">Copyright &copy; 2019 Maple Crest Yardworks</div>
</body>
</html>
```